Book Cover for my Autobiography

I would like to see a CONCEPT of the Front Cover as per the following.
a) Take me out of the FILE NAMED=1-MAIN.jpg
b) I want my Wife "Watching over me" - behind me - in the SHADOWS. You can take her image for the concept from the FILE NAMED=2-Wife Watching over me.jpg.
c) This based on the old saying that "Behind every Good Man....is a Woman".  So that's what I want to convert because my wife has always been in the background, in the "Shadows" - always supporting and encouraging me in whatever I do.
d) This book is purely for my children, wife, siblings, relatives and Friends.
e) the Book Cover has to be designed FLAT & RECTANGULAR - like the sample leather cover.  i.e. NOT viewed from an Angle.
f) The Book Title is "Paper Boats Home"
g) I have no pre-conceived ideas of design or colours or styling etc.  I want a PROFESSIONAL DESIGNER to come up with the best Overall Design that conveys the "Supportive Wife" always behind me and supporting me - While I am out front as the subject.
h) When the Design is accepted, I will provide the main photo of my wife without my son in front of her that I want to use - and one me without my wife's arms around me.  But if you can do that too (i.e. reconstruct my Wife's Burgundy top & and remove her arms from around me-then even better because I don't have to hire another graphic designer to do that for me).
My name is "Rupert ten Brakel" so the author of the autobiography needs to be SOMEWHERE.
h) And last, please just put some text - maybe 2 sentences for the summary of the story like many Autobiographies do. eg.
"My story of how ....Lorem ipsum dolor sit amet, consectetur adipiscing elit, sed do eiusmod tempor incididunt. Integer vitae justo eget magna fermentum iaculis eu non. Aliquam eleifend".

I forgot to mention that this Book Cover is actually going on an eBOOK - not a Printed Book.
It's just for Family and Friends.

```html
<!DOCTYPE html>
<html lang="en">
<head>
<meta charset="utf-8">
<title>Paper Boats Home — Rupert ten Brakel</title>
<link href="https://fonts.googleapis.com/css2?family=Bagel+Fat+One&family=Tinos&family=Cabin:wght@400&display=swap" rel="stylesheet">
<style>
  :root {
    --page: #ffffff;
    --cover: #ffffff;
    --cover-edge: #b5b5b5;
    --author-green: #1d8a4b;
    --rule-grey: #8c8c8c;
    --ghost-grey: #9a9a9a;
    --blurb-red: #e31e2d;
    --blurb-text: #ffffff;
  }
  * { margin: 0; padding: 0; box-sizing: border-box; }
  html, body {
    width: 926px;
    height: 1200px;
    overflow: hidden;
    background: var(--page);
  }
  .stage {
    position: relative;
    width: 926px;
    height: 1200px;
  }
  .book-cover {
    position: absolute;
    left: 64px;
    top: 34px;
    width: 887px;
    height: 1258px;
    background: var(--cover);
    border: 1px solid var(--cover-edge);
    transform: scale(0.9);
    transform-origin: top left;
  }
  .author {
    position: absolute;
    left: 0;
    right: 0;
    top: 114px;
    height: 64px;
  }
  .author-rule {
    position: absolute;
    left: 262px;
    width: 363px;
    height: 2px;
    background: var(--rule-grey);
  }
  .author-rule--top { top: 0; }
  .author-rule--bottom { top: 62px; }
  .author-name,
  .author-echo {
    position: absolute;
    left: 0;
    right: 0;
    text-align: center;
    font-family: "Tinos", "Times New Roman", serif;
    font-size: 46px;
    line-height: 1;
    letter-spacing: 0.5px;
    white-space: nowrap;
  }
  .author-name {
    top: 8px;
    color: var(--author-green);
  }
  .author-echo {
    top: 28px;
    color: var(--ghost-grey);
    opacity: 0.45;
    transform: scaleY(-0.55);
    transform-origin: center bottom;
  }
  .title {
    position: absolute;
    left: 104px;
    top: 314px;
    width: 710px;
    height: 650px;
    overflow: visible;
  }
  .title text {
    font-family: "Bagel Fat One", "Arial Black", sans-serif;
    font-size: 210px;
  }
  .blurb {
    position: absolute;
    left: 88px;
    top: 1048px;
    width: 711px;
    height: 100px;
    background: var(--blurb-red);
    color: var(--blurb-text);
    font-family: "Cabin", "Gill Sans", sans-serif;
    font-size: 20.5px;
    line-height: 25px;
    padding: 12px 20px 0 26px;
  }
</style>
</head>
<body>
<main class="stage">
  <article class="book-cover">
    <header class="author">
      <div class="author-rule author-rule--top"></div>
      <p class="author-echo" aria-hidden="true">RUPERT TEN BRAKEL</p>
      <p class="author-name">RUPERT TEN BRAKEL</p>
      <div class="author-rule author-rule--bottom"></div>
    </header>

    <svg class="title" viewBox="0 0 710 650" role="img"
         aria-label="Book title Paper Boats Home, its letters filled with a warm portrait of the author smiling in front with his wife behind him">
      <defs>
        <linearGradient id="title-photo-tones" x1="0" y1="0" x2="0.6" y2="1">
          <stop offset="0" stop-color="#1a2a30"/>
          <stop offset="0.25" stop-color="#7d5e55"/>
          <stop offset="0.45" stop-color="#b88e7c"/>
          <stop offset="0.62" stop-color="#1c2d34"/>
          <stop offset="0.78" stop-color="#9c7263"/>
          <stop offset="1" stop-color="#8e2e2c"/>
        </linearGradient>
      </defs>
      <g fill="url(#title-photo-tones)">
        <text x="0" y="154" textLength="710" lengthAdjust="spacingAndGlyphs">PAPER</text>
        <text transform="translate(0,482) scale(1,2.05)" x="0" y="0" textLength="710" lengthAdjust="spacingAndGlyphs">BOATS</text>
        <text x="0" y="650" textLength="710" lengthAdjust="spacingAndGlyphs">HOME</text>
      </g>
    </svg>

    <p class="blurb">"My story of how .... Lorem ipsum dolor sit amet, consectetur adipiscing elit, sed do eiusmod tempor incididunt. Integer vitae justo eget magna fermentum iaculis eu non. Aliquam eleifend".</p>
  </article>
</main>
</body>
</html>
```